sydney wedding photography business needs a business card design

we need a business card design for a sydney based wedding photography and videography business. our business name is :golden hour photography and video. our target clients are 24-35 yrs female. our style is candid, organic, natural, dynamic. we are a team of young photographers and videographers, and help brides to create memories that they will cherish for the rest of their lives. the logo will be provided. we want an elegant design that reflects our style, and also want to give a great impression to our clients that we are one of the best studios in sydney and our brand means quality and premium service.

Target Market(s)

bride to be, 24-35 years old, living in sydney and surrunding areas

Industry/Entity Type

Wedding Photography

Contact Information for Business Card

address: 57 marrow lane, bexton nsw 2041
mobile: 0431872056
phone: (02) 9361 2748
info@goldenhourstudio.net.au
www.goldenhourstudio.net.au
facebook:goldenhourbridals
instagram:goldenhourbridals

Font styles to use
Serif
Sans Serif

Requirements
Nice to have
• maybe add my slogan"memories beyond eternity" if the layout looks good
Should not have
• no black color, not good idea for wedding biz card

```html
<!DOCTYPE html>
<html lang="en">
<head>
<meta charset="utf-8">
<title>Golden Hour Photography and Video – Business Card</title>
<link rel="stylesheet" href="https://fonts.googleapis.com/css2?family=Pinyon+Script&family=Didact+Gothic&display=swap">
<style>
  :root {
    --page: #d9d6c4;
    --cream: #e9dca7;
    --ink: #2b2620;
    --brown: #5c3c19;
    --ring: #8a6336;
    --gold: #9a7128;
  }
  * { margin: 0; padding: 0; box-sizing: border-box; }
  html, body { width: 1200px; height: 854px; overflow: hidden; background: var(--page); }
  .canvas { position: relative; width: 1200px; height: 854px; }

  .card { position: absolute; width: 640px; height: 360px; overflow: hidden; box-shadow: 0 6px 18px rgba(0,0,0,.25); }

  /* Contact side */
  .card-front { left: 100px; top: 70px; background: var(--cream); z-index: 2; }
  .frame-outer { position: absolute; inset: 12px; border: 5px solid var(--ink); }
  .frame-corners { position: absolute; left: 0; top: 0; }
  .title { position: absolute; left: 0; right: 0; top: 26px; text-align: center; font-family: "Pinyon Script", cursive; color: var(--ink); }
  .title-name { font-size: 50px; line-height: 58px; }
  .title-sub { font-size: 32px; line-height: 36px; margin-top: -4px; }
  .contacts { position: absolute; font-family: "Didact Gothic", sans-serif; color: var(--ink); font-size: 16px; list-style: none; }
  .contacts li { display: flex; align-items: center; gap: 14px; height: 35px; }
  .contacts-left { left: 70px; top: 176px; }
  .contacts-right { left: 418px; top: 176px; }
  .icon { width: 22px; height: 22px; flex: none; }
  .address { position: absolute; left: 436px; top: 262px; font-family: "Didact Gothic", sans-serif; font-style: italic; font-size: 15px; line-height: 20px; color: var(--ink); }

  /* Brand side */
  .card-back { left: 490px; top: 420px; background: var(--brown); z-index: 1; }
  .back-art { position: absolute; inset: 0; }
  .brand-name { position: absolute; left: 0; right: 0; top: 138px; text-align: center; font-family: "Pinyon Script", cursive; font-size: 72px; line-height: 84px; color: var(--gold); }
</style>
</head>
<body>
<main class="canvas">

  <section class="card card-front" aria-label="Business card, contact side">
    <div class="frame-outer"></div>
    <svg class="frame-corners" width="640" height="360" viewBox="0 0 640 360" aria-hidden="true">
      <g fill="none" stroke="var(--ink)" stroke-width="5">
        <path d="M30 78 V30 H80"/>
        <path d="M560 30 H610 V78"/>
        <path d="M30 282 V330 H80"/>
        <path d="M560 330 H610 V282"/>
      </g>
    </svg>

    <header class="title">
      <div class="title-name">Golden Hour</div>
      <div class="title-sub">Photography and Video</div>
    </header>

    <ul class="contacts contacts-left">
      <li>
        <svg class="icon" viewBox="0 0 22 22" aria-hidden="true"><g fill="none" stroke="var(--ink)" stroke-width="1.4"><circle cx="11" cy="11" r="10"/><rect x="5.5" y="7" width="11" height="8" rx="1"/><path d="M5.5 7.5 L11 12 L16.5 7.5"/></g></svg>
        <span>info@goldenhourstudio.net.au</span>
      </li>
      <li>
        <svg class="icon" viewBox="0 0 22 22" aria-hidden="true"><circle cx="11" cy="11" r="10" fill="none" stroke="var(--ink)" stroke-width="1.4"/></svg>
        <span>goldenhourbridals</span>
      </li>
      <li>
        <svg class="icon" viewBox="0 0 22 22" aria-hidden="true"><g fill="none" stroke="var(--ink)" stroke-width="1.3"><circle cx="11" cy="11" r="10"/><circle cx="11" cy="11" r="6"/><ellipse cx="11" cy="11" rx="2.6" ry="6"/><path d="M5 11 H17 M6 8 H16 M6 14 H16"/></g></svg>
        <span>www.goldenhourstudio.net.au</span>
      </li>
      <li>
        <svg class="icon" viewBox="0 0 22 22" aria-hidden="true"><circle cx="11" cy="11" r="10" fill="none" stroke="var(--ink)" stroke-width="1.4"/></svg>
        <span>goldenhourbridals</span>
      </li>
    </ul>

    <ul class="contacts contacts-right">
      <li>
        <svg class="icon" viewBox="0 0 22 22" aria-hidden="true"><circle cx="11" cy="11" r="10" fill="none" stroke="var(--ink)" stroke-width="1.4"/><path d="M7 6 L9.5 6 L10.5 8.5 L9 9.8 Q10.2 12.3 12.2 13.2 L13.5 11.7 L16 12.7 L16 15 Q15 16.3 13.3 16 Q7.6 14.4 6 8.5 Q5.8 6.8 7 6 Z" fill="var(--ink)"/></svg>
        <span>(02) 9361 2748</span>
      </li>
      <li>
        <svg class="icon" viewBox="0 0 22 22" aria-hidden="true"><g fill="none" stroke="var(--ink)" stroke-width="1.4"><circle cx="11" cy="11" r="10"/><rect x="7.5" y="5" width="7" height="12" rx="1.2"/><path d="M7.5 14.5 H14.5"/></g></svg>
        <span>0431872056</span>
      </li>
    </ul>

    <address class="address">57 Marrow lane<br>Bexton nsw 2041</address>
  </section>

  <section class="card card-back" aria-label="Business card, brand side">
    <svg class="back-art" width="640" height="360" viewBox="0 0 640 360" aria-hidden="true">
      <circle cx="310" cy="180" r="236" fill="var(--cream)" stroke="var(--ring)" stroke-width="5"/>
    </svg>
    <div class="brand-name">Golden Hour</div>
  </section>

</main>
</body>
</html>
```